Business Cards and Stationery - Real Estate
See "information" and "additional comments"
Business Cards and Stationery - Real Estate - Real Estate
Creative Brief
Professional
Anselm Varga
Managing Broker
4382 SW Route 14, Ste 305 Vancouver, WA 98671
Direct - 360-555-0147
Cell - 360-555-0193
anselm@fernloftpm.example
www.fernlofthomes.example
Licensed in OR & WA
We want to use UV spotting on our cards. Here is a video link from the printing company we are using. If you are unfamiliar with creating files for UV spotting, it requires one file for the card and a second mask file for the UV spotting. https://www.clipvault.example/watch?v=Qx7rLm2PzA1 I've uploaded the template files to use from Zentra Print along with our Adobe Illustrator Logo files and a head shot. We probably don't want a head shot on the card, but have uploaded just in case. Please use Adobe Illustrator.
Probably just the logo. Something that is clean, possible a repeated design such as the logo. Would like to consider UV spotting on back. Try searching for "business cards spot uv" on Google, then look at the "images" link.
SiteAdmin SiteAdmin
Dear Designers, Kindly follow the below mention instructions by the Project holder for better and improve designs: We want to use spot UV on our cards, front and back. Here is a video Link from the printing company we are using. If you are unfamiliar with creating file for Spot UV, it requires one file for the card and a second mask file for the UV spotting. https://www.clipvault.example/watch?v=Qx7rLm2PzA1 Use your creativity, but a couple ideas for the back would be to repeat our logo over and over across the entire back. It may be nice to somehow put our website within those repeated logos. Or it may not be nice, depending on how it looks. You could also just make our logo with URL on the back. For the front, you will have to be creative to make it work. Our logo could be UV spotted. And then probably some sort of nice design that covers a portion of the front, keeping in mind that the uv spot coating design can overlap anything. Or maybe it would look best to only spot uv our logo. The content for the card is in our creative brief. We would also like to include "We Love Referrals!" somewhere on the card. Here are a few images for some ideas. Keep in mind that we don't want a copy of what is done with these ideas. They are simply ideas of what can be done with UV spotting. https://pressglow.example/assets/images/gallery/business-cards/images/a1b2c3d4e5f60718293a4b5c6d7e8f90.png https://pressglow.example/assets/uploads/spot_uv_marlow_business_cards.jpg http://media.shopweave.example/51730264/Renata-Pell-spot-gloss-silver-foil-spot-uv-silk-unique-cool-business-cards_full.jpeg http://www.quartzlinecards.example/images/img-gallery/silk-business-card-with-spot-uv-harrow-cellars.jpg http://i01.i.tradepix.example/wsphoto/v2/813406572_2/Custom-Spot-UV-business-card-matt-coated-paper-350gsm-High-quality.jpg http://www.newswire.example/64028195-silk-laminated-business-cards-with-spot-uv.jpg http://www.atelier-cartes-nord.example/wp-content/uploads/2010/10/carte-commerciale-vernis-selectif.jpg https://pressglow.example/assets/uploads/spot_uv_cards_dravetek.jpg http://www.calloutmailers.example/wp/wp-content/uploads/2013/03/zebra-orange-spot-uv-business-card1.png http://layoutharbor.example/wp-content/uploads/2013/04/square-business-card-29.jpg
fernloft47 fernloft47
I forgot to add on that last comment, that the black designs are way to dark for our tastes. Blue on the back looks nice. We prefer the lighter designs on the front of the card.
We are looking for double sided cards with rounded corners and some UV spotting on both sides. We like the design of #96 on the back side, however it looks like there may be some silver foil on the logo. We won't be doing foil, just spotting. There are a lot of nice designs so far, but we need to have the combination of rounded corners and UV spotting. Thanks.

```html
<!DOCTYPE html>
<html lang="en">
<head>
<meta charset="utf-8">
<title>Fernloft Properties – Business Card</title>
<link href="https://fonts.googleapis.com/css2?family=Montserrat:wght@600;700&family=Open+Sans:wght@400;600&display=swap" rel="stylesheet">
<style>
  :root {
    --page-bg: #e9eaec;
    --card-white: #ffffff;
    --brand-blue: #2b5d9c;
    --deep-blue: #1f4a80;
    --wave-grey: #9a9fa6;
    --ink: #2c3440;
    --soft-white: #dbe5f2;
  }
  html, body {
    margin: 0;
    width: 1200px;
    height: 901px;
    overflow: hidden;
    background: var(--page-bg);
  }
  .stage {
    width: 1200px;
    height: 901px;
    display: flex;
    align-items: center;
    justify-content: center;
  }
  .business-card {
    width: 1000px;
    height: 572px;
    border-radius: 44px;
    overflow: hidden;
    background: var(--card-white);
    box-shadow: 0 10px 30px rgba(0,0,0,0.12);
  }
  .business-card svg { display: block; }
  .brand-name {
    font-family: "Montserrat", sans-serif;
    font-weight: 700;
    font-size: 34px;
    letter-spacing: 1px;
    fill: var(--brand-blue);
  }
  .person-name {
    font-family: "Open Sans", sans-serif;
    font-weight: 600;
    font-size: 24px;
    letter-spacing: 1px;
    fill: var(--ink);
  }
  .person-title {
    font-family: "Open Sans", sans-serif;
    font-weight: 400;
    font-size: 18px;
    fill: var(--brand-blue);
  }
  .address, .contact-line, .license-note, .referral-note {
    font-family: "Open Sans", sans-serif;
    fill: var(--card-white);
  }
  .address { font-size: 22px; font-weight: 400; }
  .license-note { font-size: 16px; font-weight: 400; fill: var(--soft-white); }
  .referral-note { font-size: 22px; font-weight: 600; }
  .contact-line { font-size: 19px; font-weight: 400; }
  .contact-small { font-size: 16px; }
  .contact-icon { fill: var(--card-white); }
</style>
</head>
<body>
<main class="stage">
  <section class="business-card">
    <svg width="1000" height="572" viewBox="0 0 1000 572" xmlns="http://www.w3.org/2000/svg">
      <path class="wave-grey-band" fill="var(--wave-grey)" d="M0,378 C250,410 450,340 600,232 C720,145 850,108 1000,96 L1000,130 C850,140 720,175 600,262 C450,370 250,430 0,412 Z"/>
      <path class="wave-blue-band" fill="var(--brand-blue)" d="M0,412 C250,432 450,372 600,268 C720,182 850,146 1000,136 L1000,572 L0,572 Z"/>
      <path class="wave-line" fill="none" stroke="var(--deep-blue)" stroke-width="3" d="M0,398 C250,428 450,358 600,252 C720,166 850,128 1000,116"/>

      <g class="brand">
        <rect x="80" y="128" width="46" height="46" rx="6" fill="var(--brand-blue)"/>
        <text class="brand-name" x="142" y="164">FERNLOFT PROPERTIES</text>
      </g>

      <text class="person-name" x="150" y="340">ANSELM VARGA</text>
      <text class="person-title" x="150" y="366">Managing Broker</text>

      <text class="address" x="60" y="466">4382 SW Route 14, Ste 305</text>
      <text class="address" x="60" y="496">Vancouver, WA 98671</text>
      <text class="license-note" x="60" y="530">Licensed in OR &amp; WA</text>

      <g class="contacts">
        <text class="contact-line" x="905" y="240" text-anchor="end">360-555-0147</text>
        <path class="contact-icon" d="M922,226 c2,-3 5,-3 6,-1 l3,4 c1,2 0,3 -1,4 c1,3 4,6 7,7 c1,-1 2,-2 4,-1 l4,3 c2,1 2,4 -1,6 c-10,3 -24,-11 -22,-22z"/>

        <text class="contact-line" x="905" y="282" text-anchor="end">360-555-0193</text>
        <rect class="contact-icon" x="924" y="264" width="14" height="24" rx="3"/>

        <text class="contact-line contact-small" x="905" y="322" text-anchor="end">anselm@fernloftpm.example</text>
        <circle class="contact-icon" cx="931" cy="316" r="8"/>

        <text class="contact-line contact-small" x="905" y="360" text-anchor="end">www.fernlofthomes.example</text>
        <circle cx="931" cy="354" r="8" fill="none" stroke="var(--card-white)" stroke-width="2.5"/>
      </g>

      <text class="referral-note" x="940" y="520" text-anchor="end">We Love Referrals!</text>
    </svg>
  </section>
</main>
</body>
</html>
```